New Record Label needs a Web design

We are Moss Lantern: a London based, new & independent music production company aimed at the 25-40 age group. The musical style is Soul/Classic Motown.
We have at the moment just one signed artist, but will expand in the future.
We dont' have any webpage yet and are looking for an innovative web design for our webpage www.moss-lantern.com
I have uploaded our company logo.

Initially the whole website will only have 3 tabs: Home page/Artists/Contact

The design should be classic and high-end, but can be a bit crazy too.

```html
<!DOCTYPE html>
<html lang="en">
<head>
<meta charset="utf-8">
<title>Moss Lantern — Soul &amp; Classic Records</title>
<link href="https://fonts.googleapis.com/css2?family=Open+Sans:wght@400;600;700&display=swap" rel="stylesheet">
<style>
  :root{
    --ink:#ffffff;
    --muted:#d6d6d6;
    --red:#e63a35;
    --orange:#e8662f;
    --header:#1e1e1e;
    --nav-active:#111111;
    --player-band:#555555;
    --panel-black:#040404;
    --panel-dark:#1b1b1b;
    --footer:#1c1c1c;
    --crowd-a:#d9d9d9;
    --crowd-b:#f1f1f1;
  }
  *{box-sizing:border-box;margin:0;padding:0}
  html,body{width:845px;height:1200px;overflow:hidden;background:#fff}
  body{font-family:"Open Sans",Arial,sans-serif;color:var(--ink);position:relative}
  .abs{position:absolute}

  .site{position:absolute;left:13px;top:15px;width:815px;height:1163px;overflow:hidden;
    background:linear-gradient(160deg,var(--crowd-a),var(--crowd-b) 45%,var(--crowd-a));}

  /* header */
  .header{left:0;top:0;width:815px;height:68px;background:var(--header);border-bottom:2px solid var(--red)}
  .brand{left:125px;top:16px;display:flex;align-items:center;gap:10px}
  .brand-dot{width:34px;height:34px;border-radius:50%;background:var(--red)}
  .brand-name{font-size:24px;font-weight:600;color:var(--red)}
  .nav{left:451px;top:0;display:flex;height:68px}
  .nav a{display:flex;align-items:center;gap:6px;height:68px;padding:0 12px;color:var(--ink);
    text-decoration:none;font-size:10.5px;text-transform:uppercase;border-right:1px solid #2a2a2a}
  .nav a.active{background:var(--nav-active);font-weight:700}
  .nav svg{width:13px;height:13px;fill:#fff}
  .nav a.active svg{fill:var(--red)}

  /* slider */
  .slider{left:0;top:70px;width:815px;height:233px;
    background:radial-gradient(ellipse at 50% 30%,#5a58d8 0%,#3a2f9a 35%,#1a1440 75%,#0d0a1c 100%)}
  .slide-arrow{top:97px;width:26px;height:24px}
  .slide-caption{left:0;width:815px;top:176px;text-align:center;font-size:23px;font-weight:700;letter-spacing:.3px}
  .slide-dots{left:389px;top:216px;display:flex;gap:4px}
  .slide-dots span{width:10px;height:10px;border-radius:50%;border:2px solid #fff;background:#000}
  .slide-dots span.on{background:var(--red)}

  /* player */
  .player-band{left:0;top:303px;width:815px;height:72px;background:var(--player-band)}
  .player-title{left:0;width:815px;top:13px;text-align:center;font-size:14.5px;font-weight:700}
  .player-buttons{left:136px;top:43px;display:flex;gap:6px;align-items:center}
  .player-buttons span{border:1.5px solid #fff;border-radius:50%;display:flex;align-items:center;justify-content:center}
  .player{left:211px;top:43px;width:464px;height:22px;background:#fff;border-radius:2px;
    display:flex;align-items:center;font-size:7px;color:#888}
  .track{position:relative;height:2px;background:#bbb}
  .track i{position:absolute;left:0;top:0;height:2px;background:var(--orange)}

  /* content column */
  .about{left:125px;top:377px;width:566px;height:226px;background:var(--panel-black);padding:18px 23px}
  .section-title{text-align:center;font-size:16.5px;font-weight:600}
  .section-title em{font-style:normal;color:var(--red)}
  .about p{font-size:9.6px;line-height:18.2px;text-align:justify;color:#e8e8e8;margin-top:6px}
  .about p + p{margin-top:17px}

  .artists{left:125px;top:605px;width:566px;height:302px;background:var(--panel-dark);padding-top:12px}
  .artists .section-title{font-size:14.5px}
  .artist{position:absolute;top:51px;width:130px;text-align:center;font-size:11.5px;font-weight:600}
  .portrait{width:128px;height:128px;border-radius:50%;border:2px solid #fff;margin:0 auto 10px;
    box-shadow:0 3px 6px rgba(0,0,0,.6)}
  .portrait.featured{border:3px solid var(--red)}
  .carousel-arrow{top:110px;width:20px;height:18px}
  .btn-artists{left:214px;top:248px;width:137px;height:30px;background:linear-gradient(#f07a3c,#e25a24);
    display:flex;align-items:center;justify-content:center;gap:7px;font-size:11.5px;border-radius:1px}

  /* footer */
  .footer{left:125px;top:907px;width:566px;height:158px;background:var(--footer);border-top:3px solid var(--red)}
  .col{position:absolute;top:30px}
  .col h4{font-size:11px;font-weight:600;display:flex;align-items:center;gap:4px}
  .col h4 svg{width:11px;height:11px;fill:var(--red)}
  .links{list-style:none;margin-top:4px;width:100px}
  .links li{font-size:9px;padding:4px 0 5px 6px;border-bottom:1px solid #3a3a3a}
  .links li.current{color:var(--red);font-weight:700}
  .tweet{font-size:8px;line-height:12px;padding-left:16px;margin-top:8px}
  .tweet a{color:var(--red);text-decoration:none;display:block}
  .tweet time{display:block;font-size:7px;margin-top:8px}
  .thumbs{display:grid;grid-template-columns:repeat(3,36px);gap:3px 9px;margin-top:6px}
  .thumbs span{height:33px;background:linear-gradient(135deg,#6a5a8e,#2b2640)}
  .thumbs span:nth-child(2n){background:linear-gradient(135deg,#c0603a,#3a2a2a)}
  .thumbs span:nth-child(3n){background:linear-gradient(135deg,#3b6fd1,#231b4a)}
  .signup-field{width:137px;height:19px;background:#0c0c0c;border:1px solid #2e2e2e;font-size:7.5px;
    color:#666;padding:4px 6px;margin-top:8px}
  .socials{display:flex;gap:5px;margin-top:18px}
  .socials span{width:18px;height:18px;border-radius:3px;background:#4d7fc0}
  .socials span:nth-child(2){background:#2fa6c9}
  .socials span:nth-child(3){background:#c24444}
  .btn-submit{position:absolute;left:79px;top:66px;width:57px;height:24px;background:var(--red);
    font-size:11px;font-weight:700;display:flex;align-items:center;justify-content:center}

  .contact-band{left:125px;top:1065px;width:566px;height:70px;background:#000;text-align:center}
  .contact-name{font-size:16.5px;color:var(--red);margin-top:8px;text-transform:uppercase}
  .contact-line{font-size:11px;margin-top:6px;display:flex;justify-content:center;gap:8px;align-items:center}
  .contact-line svg{width:11px;height:11px;fill:var(--orange);vertical-align:-1px;margin-right:3px}
  .legal{left:125px;top:1135px;width:566px;height:28px;background:var(--footer);font-size:7px;
    display:flex;justify-content:space-between;align-items:center;padding:0 20px}
</style>
</head>
<body>
<div class="site">
  <div class="abs" role="img" aria-label="Greyscale photo of a concert crowd with raised hands" style="inset:375px 0 0 0"></div>

  <header class="header abs">
    <div class="brand abs"><span class="brand-dot"></span><span class="brand-name">Moss Lantern</span></div>
    <nav class="nav abs">
      <a class="active" href="#"><svg viewBox="0 0 16 16"><path d="M8 1 0 8h2v7h4v-4h4v4h4V8h2z"/></svg>Home</a>
      <a href="#"><svg viewBox="0 0 16 16"><circle cx="5" cy="5" r="3"/><circle cx="11" cy="5" r="3"/><path d="M0 15c0-4 2-6 5-6s5 2 5 6zM9 15c0-3 0-5 2-6 3 0 5 2 5 6z"/></svg>Artists</a>
      <a href="#"><svg viewBox="0 0 16 16"><ellipse cx="7" cy="6" rx="7" ry="5"/><path d="M3 10 2 15 7 11z"/></svg>Contact</a>
    </nav>
  </header>

  <section class="slider abs" role="img" aria-label="Soul band performing on a blue-lit stage with singers and a guitarist">
    <svg class="slide-arrow abs" style="left:22px" viewBox="0 0 26 24"><path d="M0 12 12 0v7h14v10H12v7z" fill="#fff"/></svg>
    <svg class="slide-arrow abs" style="left:773px" viewBox="0 0 26 24"><path d="M26 12 14 0v7H0v10h14v7z" fill="#fff"/></svg>
    <p class="slide-caption abs">I LOVE SOUL/CLASSIC MUSIC</p>
    <div class="slide-dots abs"><span class="on"></span><span></span><span></span></div>
  </section>

  <section class="player-band abs">
    <h2 class="player-title abs">Our New Classic Out</h2>
    <div class="player-buttons abs">
      <span style="width:16px;height:16px"><svg width="8" height="6" viewBox="0 0 8 6"><path d="M4 0v6L0 3zM8 0v6L4 3z" fill="#fff"/></svg></span>
      <span style="width:20px;height:20px"><svg width="8" height="9" viewBox="0 0 8 9"><path d="M1 0v9l7-4.5z" fill="#fff"/></svg></span>
      <span style="width:16px;height:16px"><svg width="8" height="6" viewBox="0 0 8 6"><path d="M0 0v6l4-3zM4 0v6l4-3z" fill="#fff"/></svg></span>
    </div>
    <div class="player abs">
      <span style="margin-left:10px">00:02</span>
      <div class="track" style="width:260px;margin-left:10px"><i style="width:42px"></i></div>
      <span style="margin-left:10px">00:15</span>
      <div style="margin-left:10px;height:22px;width:94px;background:#eee;display:flex;align-items:center;gap:4px;padding-left:8px">
        <svg width="7" height="7" viewBox="0 0 7 7"><path d="M0 2h2l3-2v7L2 5H0z" fill="#555"/></svg>
        <div class="track" style="width:55px;background:#bbb"><i style="width:46px"></i></div>
        <svg width="7" height="7" viewBox="0 0 7 7"><path d="M0 2h2l3-2v7L2 5H0z" fill="#555"/></svg>
      </div>
      <svg style="margin-left:12px" width="7" height="6" viewBox="0 0 7 6"><path d="M0 0h7v1H0zM0 2.5h7v1H0zM0 5h7v1H0z" fill="#555"/></svg>
    </div>
  </section>

  <section class="about abs">
    <h1 class="section-title">Hello we’re <em>Moss Lantern</em></h1>
    <p>In elementum pellentesque dolor ac gravida. Pellentesque elit leo, accumsan sed consectetur a, semper ac sem. Morbi sodales bibendum risus nec laoreet. Mauris est nisi, consequat vitae porta et, hendrerit sed metus. Aliquam eu magna vel metus ultrices ornare in et nisi. Quisque porta sodales orci, eu auctor leo tincidunt nec. Suspendisse posuere blandit tortor sit amet varius. Integer condimentum rutrum mi quis lobortis. Etiam consectetur posuere pretium.</p>
    <p>Aliquam eu magna vel metus ultrices ornare in et nisi. Quisque porta sodales orci, eu auctor leo tincidunt nec. Suspendisse posuere blandit tortor sit amet varius. Integer condimentum rutrum mi quis lobortis. Etiam consectetur posuere pretium.</p>
  </section>

  <section class="artists abs">
    <h2 class="section-title">Future Artists</h2>
    <svg class="carousel-arrow abs" style="left:12px" viewBox="0 0 20 18"><path d="M0 9 9 0v5h11v8H9v5z" fill="#fff"/></svg>
    <svg class="carousel-arrow abs" style="left:537px" viewBox="0 0 20 18"><path d="M20 9 11 0v5H0v8h11v5z" fill="#fff"/></svg>
    <div class="artist" style="left:44px"><div class="portrait featured" role="img" aria-label="Portrait of Ravi Dunmore in beanie and headphones" style="background:linear-gradient(#eee,#9a9a9a)"></div>Ravi Dunmore</div>
    <div class="artist" style="left:218px"><div class="portrait" role="img" aria-label="Portrait of Tessa Crane singing on a purple-lit stage" style="background:radial-gradient(#b34ad9,#3a1060)"></div>Tessa Crane</div>
    <div class="artist" style="left:394px"><div class="portrait" role="img" aria-label="Portrait of Owen Hartley singing at a microphone" style="background:radial-gradient(#c06ab0,#4a2050)"></div>Owen Hartley</div>
    <div class="btn-artists abs">
      <svg width="16" height="13" viewBox="0 0 16 13"><circle cx="8" cy="3" r="3" fill="#fff"/><circle cx="3" cy="4" r="2" fill="#fff"/><circle cx="13" cy="4" r="2" fill="#fff"/><path d="M3 13c0-4 2-6 5-6s5 2 5 6zM0 12c0-3 1-5 3-5l1 1-1 4zM16 12c0-3-1-5-3-5l-1 1 1 4z" fill="#fff"/></svg>
      View All Artists
    </div>
  </section>

  <footer class="footer abs">
    <div class="col" style="left:8px">
      <h4><svg viewBox="0 0 12 12"><path d="M4 0h4v3H7v2h4v3h1v4H8V8h1V6H3v2h1v4H0V8h1V5h4V3H4z"/></svg>Browse Around</h4>
      <ul class="links"><li class="current">Home</li><li>Artists</li><li>Contact</li></ul>
    </div>
    <div class="col" style="left:142px">
      <h4><svg viewBox="0 0 12 12"><circle cx="6" cy="6" r="5"/></svg>Social Feed</h4>
      <p class="tweet">resume template<a href="#">HTTP://ml.to/q7rxbn</a><time>July 01, 2014 07:56:37</time></p>
    </div>
    <div class="col" style="left:278px">
      <h4><svg viewBox="0 0 12 12"><rect x="0" y="1" width="12" height="10" rx="2"/></svg>Photo Feed</h4>
      <div class="thumbs" role="img" aria-label="Six small live concert photos">
        <span></span><span></span><span></span><span></span><span></span><span></span>
      </div>
    </div>
    <div class="col" style="left:420px">
      <h4><svg viewBox="0 0 12 12"><path d="M0 2h12v1L6 7 0 3zM0 4.5l6 4 6-4V10H0z"/></svg>Newsletter Signup</h4>
      <div class="signup-field">Enter your email address</div>
      <div class="socials"><span></span><span></span><span></span></div>
      <div class="btn-submit">Submit</div>
    </div>
  </footer>

  <section class="contact-band abs">
    <h3 class="contact-name">Moss Lantern</h3>
    <p class="contact-line">
      <span><svg viewBox="0 0 12 12"><path d="M6 0a4 4 0 0 0-4 4c0 3 4 8 4 8s4-5 4-8a4 4 0 0 0-4-4zm0 5.5A1.5 1.5 0 1 1 6 2.5a1.5 1.5 0 0 1 0 3z"/></svg>42 Kestrel Lane, London, NW7 2QD</span>|
      <span><svg viewBox="0 0 12 12"><path d="M2 0h2l1 3-1.5 1.5a7 7 0 0 0 4 4L9 7l3 1v2c0 1-1 2-2 2A10 10 0 0 1 0 2c0-1 1-2 2-2z"/></svg>0800.555.7304</span>&nbsp;&nbsp;|
      <span><svg viewBox="0 0 12 12"><path d="M0 2h12v1L6 7 0 3zM0 4.5l6 4 6-4V10H0z"/></svg>hello@mosslantern.com</span>
    </p>
  </section>

  <div class="legal abs">
    <span>© Copyright 2014 Moss Lantern. All rights reserved.</span>
    <span>Privacy Policy &nbsp;|&nbsp; Term &amp; Conditions</span>
  </div>
</div>
</body>
</html>
```